Harlow Ironworks Business Card

We need a business card design for a new small metal fabrication business in rural NSW, Australia.

The business (Harlow Ironworks) is owner operated by a man with the initials KB - much of the branding comes from this name.

Harlow Ironworks designs, engineers, repairs and manufactures a range of custom, quality metal works including vehicle trays, agricultural machinery impliments, trailers, wood splitters, fire pits, furniture etc.

The brand position focuses on custom work of the highest quality.

Business card design should show quality, attention to detail and stand out among a mass of business cards.

Logos are in the files

The grey color may be changed on the logo if required to stand out more.

There is an image attached of a simple card that is liked because it is clean, clear, simple, masculine and effective. It says 'quality'. As most of the work we do is custom it would be good to have the business card speak to this.

Target Market(s)

Rural and regional based Australians. Primarily adult male 25-60 yrs. Primary production / rural / travelling lifestyle.

Industry/Entity Type

Metal Fabrication

Contact Information for Business Card

The words 'custom quality fabrications' would be great somewhere perhaps on the backside (not on the information side)
Name
title
Phone: 0418 539 746 and (02) 6193 4827
email: info@harlowiw.com.au
www.harlowiw.com.au

address (2 lines)

Requirements
Nice to have
• Background colour should be very navy blue or black.
Should not have
• NO orange and blue combinations.
• Navy is OK

```html
<!DOCTYPE html>
<html lang="en">
<head>
<meta charset="utf-8">
<title>Harlow Ironworks Business Card</title>
<link rel="stylesheet" href="https://fonts.googleapis.com/css2?family=Source+Sans+3:wght@400;600;700&display=swap">
<style>
  :root {
    --backdrop: #aaaaaa;
    --card: #141414;
    --accent: #6cc04a;
    --text-light: #e8e8e8;
    --brand-grey: #a9a9a9;
  }
  * { margin: 0; padding: 0; box-sizing: border-box; }
  html, body {
    width: 1200px;
    height: 900px;
    overflow: hidden;
    background: var(--backdrop);
    font-family: "Source Sans 3", Arial, sans-serif;
  }
  .canvas {
    position: relative;
    width: 1200px;
    height: 900px;
  }
  .card {
    position: absolute;
    top: 215px;
    width: 414px;
    height: 414px;
    border-radius: 50%;
    background: var(--card);
    text-align: center;
    color: var(--text-light);
  }
  .card--info { left: 164px; }
  .card--brand { left: 623px; }

  .info {
    position: absolute;
    left: 0;
    right: 0;
    top: 82px;
    font-size: 18px;
    line-height: 25px;
  }
  .info__name {
    color: var(--accent);
    font-weight: 700;
    font-size: 20px;
    line-height: 24px;
  }
  .info__title { margin-bottom: 42px; }
  .label { color: var(--accent); font-weight: 700; }
  .phone + .phone { margin-left: 10px; }
  .info__web { color: var(--accent); font-weight: 700; margin-bottom: 33px; }

  .brand {
    position: absolute;
    left: 0;
    right: 0;
    top: 118px;
  }
  .brand__mark {
    display: block;
    margin: 0 auto 48px;
  }
  .brand__name {
    color: var(--brand-grey);
    font-weight: 700;
    font-size: 36px;
    line-height: 40px;
    letter-spacing: 3px;
    text-transform: uppercase;
  }
</style>
</head>
<body>
<main class="canvas">
  <section class="card card--info">
    <div class="info">
      <p class="info__name">KIERAN BELL</p>
      <p class="info__title">Managing Director</p>
      <p class="info__phones">
        <span class="phone"><span class="label">P:</span> 0418 539 746</span>
        <span class="phone"><span class="label">P:</span> (02) 6193 4827</span>
      </p>
      <p class="info__email"><span class="label">E:</span> info@harlowiw.com.au</p>
      <p class="info__web">www.harlowiw.com.au</p>
      <p class="info__address">Addres Line Comes Here,<br>Location Pincode 45215</p>
    </div>
  </section>

  <section class="card card--brand">
    <div class="brand">
      <svg class="brand__mark" width="60" height="60" viewBox="0 0 60 60" aria-hidden="true">
        <rect x="0" y="0" width="60" height="60" fill="var(--accent)"/>
      </svg>
      <p class="brand__name">Harlow<br>Ironworks</p>
    </div>
  </section>
</main>
</body>
</html>
```